Zielgruppe
Die Tafel Depot verkauft Lebensmittel mit abgelaufene MHD (Mindesthaltbarkeitsdatum), Waren aus Überproduktion ; Startup Produkte, die es nicht in den Verkauf bei den grossen Lebensmittelkonzerne wie Talo / Morvi und co. geschafft haben oder aus diversen Überproduktionen.
Wir haben unsere erste Filiale in Berlin NeuKöln eröffnet und unsere Kundenschaft ist bunt gemischt; von Hipstern bis konservativen Rentnern, alle lieben unser Nachhaltigkeitskonzept.
Wir bieten sehr viel Bio und Vegane Produkte an, z.B Müsli, Granola, Getreideprodukte, Brot, Getränke wie z.b Bio Mate, Chia Drinks, Bio Weine und Obst, Gemüse , Snacks und sehr viele 'unknown ' Startup Brands aus Deutschland.
Wir kaufen die Lebensmittel von den Produzenten direkt ein und prüfen diese auf Qualität.
Dadurch ist unser 'Outlet' nicht ein 'Reste Rampe' Outlet, sondern ein Konzept mit ausgewählten Produkten für ein ausgewogenes und trendiges Lebensgefühl.
Aufgabenstellung
Food Flyer mit 50% Rabatt auf jeden Einkauf im Laden.
Vorderseite :
TAFELDEPOT Logo (siehe Anhang) / NEUERÖFFNUNG und Adresse :
Öffnungszeiten : 10-20 Uhr Mo-Sa
Rückseite:
Platzhalter für 8 Bestseller mit 'normalen Preis' und im Vergleich unser reduzierter Preis . Der Apfel ist unser Rabatt Maskottchen. Sei kreativ UND Wir haben auch eine Austausch Garantie ; bei schlechter Qualität oder Defekt gibt es ein Austauschprodukt

```html
<!DOCTYPE html>
<html lang="de">
<head>
<meta charset="utf-8">
<title>Tafel Depot – Flyer</title>
<link rel="stylesheet" href="https://fonts.googleapis.com/css2?family=Open+Sans:wght@300;400;600;700&display=swap">
<style>
  :root {
    --red: #bd0a2e;
    --lime: #c8d42b;
    --white: #ffffff;
    --page: #ffffff;
    --mascot: #d9e36a;
  }
  * { margin: 0; padding: 0; box-sizing: border-box; }
  html, body { width: 855px; height: 1200px; overflow: hidden; background: var(--page); }
  body { position: relative; font-family: "Open Sans", Arial, sans-serif; }

  .flyer-side {
    position: absolute;
    left: 147px;
    width: 560px;
    height: 335px;
    background: var(--white);
    box-shadow: 0 2px 8px rgba(0,0,0,0.35);
    overflow: hidden;
  }
  .flyer-front { top: 149px; }
  .flyer-back { top: 621px; }

  .flyer-side > svg.backdrop { position: absolute; inset: 0; }

  /* Front */
  .brand {
    position: absolute; left: 100px; top: 33px;
    display: flex; align-items: center; gap: 14px;
  }
  .brand-dot {
    width: 58px; height: 58px; border-radius: 50%;
    background: var(--red);
  }
  .brand-name {
    font-weight: 600; font-size: 43px; color: var(--red);
    letter-spacing: -1px; line-height: 1;
  }
  .contact-line {
    position: absolute; left: 182px; top: 90px;
    font-size: 10px; color: var(--red);
  }
  .offer-line {
    position: absolute; left: 0; right: 0; top: 126px;
    text-align: center; font-weight: 700; font-size: 19px; color: var(--red);
    padding-left: 58px;
  }
  .offer-line .accent { color: var(--lime); }
  .discount {
    position: absolute; left: 92px; top: 130px;
    font-family: Arial, "Helvetica Neue", sans-serif; font-weight: 700;
    font-size: 172px; line-height: 1; color: var(--red); letter-spacing: -4px;
    white-space: nowrap;
  }

  /* Back */
  .guarantee {
    position: absolute; right: 9px; top: 40px; text-align: right; color: var(--red);
  }
  .guarantee-title { font-weight: 700; font-size: 17.5px; line-height: 1.1; }
  .guarantee-note { font-size: 9.5px; }
  .alert-word {
    position: absolute; left: 26px; top: 113px;
    font-weight: 700; font-size: 31px; color: var(--red);
    transform: rotate(-7deg); transform-origin: left bottom;
  }
  .mascot {
    position: absolute; left: 187px; top: 22px; width: 102px; height: 120px;
    border-radius: 50% 50% 44% 44%;
    background: radial-gradient(circle at 50% 45%, var(--mascot), var(--red) 80%);
  }
  .price-arrow { position: absolute; left: 212px; top: 134px; width: 100px; height: 80px; }
  .price-arrow .arrow-label {
    position: absolute; left: 8px; top: 4px; width: 82px;
    text-align: center; font-weight: 700; font-size: 12.5px; line-height: 1.25;
    color: var(--red); transform: rotate(-9deg);
  }

  .product-grid {
    position: absolute; left: 19px; top: 189px;
    display: grid; grid-template-columns: 236px 236px; column-gap: 41px; row-gap: 8px;
  }
  .product { position: relative; height: 39px; }
  .product-thumb {
    position: absolute; left: 0; top: 0; width: 39px; height: 39px; background: var(--white);
  }
  .product-old {
    position: absolute; left: 49px; top: 11px;
    font-weight: 300; font-size: 12.5px; color: var(--white); white-space: nowrap;
  }
  .product-new {
    position: absolute; right: 0; top: 24px;
    font-weight: 300; font-size: 12.5px; color: var(--white); white-space: nowrap;
  }
  .product-new strong { font-weight: 700; font-size: 16.5px; }
</style>
</head>
<body>

<section class="flyer-side flyer-front">
  <svg class="backdrop" width="560" height="335" viewBox="0 0 560 335" aria-hidden="true">
    <path d="M0,317 C200,313 330,309 400,292 C470,275 520,245 545,205 L560,335 L0,335 Z" fill="var(--lime)"/>
    <path d="M0,327 C200,322 330,320 405,302 C485,282 552,235 560,166 L560,335 L0,335 Z" fill="var(--red)"/>
  </svg>
  <div class="brand">
    <span class="brand-dot"></span>
    <span class="brand-name">TafelDepot</span>
  </div>
  <p class="contact-line">Standort, Adresse • Telefonnummer • www.homepage.de</p>
  <p class="offer-line"><span class="accent">Rabatt</span> auf jeden Einkauf im Laden!</p>
  <p class="discount">50 %</p>
</section>

<section class="flyer-side flyer-back">
  <svg class="backdrop" width="560" height="335" viewBox="0 0 560 335" aria-hidden="true">
    <path d="M0,177 C120,160 230,148 310,147 C400,146 480,160 560,177 L560,335 L0,335 Z" fill="var(--red)"/>
    <path d="M0,184 C120,167 230,155 310,154 C400,153 480,165 560,178 L560,335 L0,335 Z" fill="var(--lime)"/>
  </svg>

  <div class="guarantee">
    <p class="guarantee-title">Unsere Austausch Garantie</p>
    <p class="guarantee-note">Bei schlechter Qualität oder Defekt gibt es ein neues!</p>
  </div>

  <p class="alert-word">Achtung!</p>

  <div class="mascot" role="img" aria-label="Apfel-Maskottchen hält einen fallenden Preispfeil"></div>

  <div class="price-arrow">
    <svg width="100" height="80" viewBox="0 0 100 80" aria-hidden="true">
      <polygon points="4,3 95,3 56,77" fill="var(--lime)" stroke="var(--white)" stroke-width="1.2"/>
    </svg>
    <p class="arrow-label">Fallender Preis!</p>
  </div>

  <div class="product-grid">
    <div class="product"><span class="product-thumb"></span><span class="product-old">Produkt 12,95 €</span><span class="product-new">Jetzt nur <strong>6,48€</strong></span></div>
    <div class="product"><span class="product-thumb"></span><span class="product-old">Produkt 12,95 €</span><span class="product-new">Jetzt nur <strong>6,48€</strong></span></div>
    <div class="product"><span class="product-thumb"></span><span class="product-old">Produkt 12,95 €</span><span class="product-new">Jetzt nur <strong>6,48€</strong></span></div>
    <div class="product"><span class="product-thumb"></span><span class="product-old">Produkt 12,95 €</span><span class="product-new">Jetzt nur <strong>6,48€</strong></span></div>
    <div class="product"><span class="product-thumb"></span><span class="product-old">Produkt 12,95 €</span><span class="product-new">Jetzt nur <strong>6,48€</strong></span></div>
    <div class="product"><span class="product-thumb"></span><span class="product-old">Produkt 12,95 €</span><span class="product-new">Jetzt nur <strong>6,48€</strong></span></div>
  </div>
</section>

</body>
</html>
```